Pediatric Dentist Business Card

I need a business card designed for a dentist who works exclusively with children.
We prefer designs that are out of ordiary that is fun and interesting to kids.

there is no logo since this is a dentists office. The name of the doctor is "Tavor Kesh" if you want to get creative with that.

Target Market(s)

Kids

Industry/Entity Type

Business

Contact Information for Business Card

Anythings that is creative

Colors

Designer to choose colors to be used in the design.

```html
<!DOCTYPE html>
<html lang="en">
<head>
<meta charset="utf-8">
<title>Tavor Kesh – Pediatric Dentist Business Card</title>
<link rel="stylesheet" href="https://fonts.googleapis.com/css2?family=Tinos:wght@400;700&display=swap">
<style>
  :root {
    --page-bg: #e4e5e8;
    --brand-red: #e51a1a;
    --brand-blue: #0a63b5;
    --paper: #ffffff;
    --shadow: rgba(0, 0, 0, 0.22);
  }
  * { box-sizing: border-box; margin: 0; padding: 0; }
  html, body {
    width: 1200px;
    height: 1200px;
    overflow: hidden;
    background: var(--page-bg);
    font-family: "Tinos", "Times New Roman", serif;
  }
  .sheet {
    position: relative;
    width: 1200px;
    height: 1200px;
  }
  .card {
    position: absolute;
    left: 160px;
    width: 880px;
    height: 510px;
    background: var(--paper);
    box-shadow: 0 14px 34px var(--shadow);
    overflow: hidden;
  }

  /* Front */
  .card--front {
    top: 60px;
    background: var(--brand-blue);
    padding: 30px;
  }
  .front-frame {
    width: 100%;
    height: 100%;
    background: var(--paper);
    border: 3px solid var(--brand-red);
    display: flex;
    align-items: center;
    justify-content: center;
    gap: 22px;
  }
  .front-mark {
    width: 58px;
    height: 58px;
    border-radius: 50%;
    background: var(--brand-blue);
  }
  .front-name {
    color: var(--brand-red);
    font-weight: 700;
    font-size: 92px;
    letter-spacing: 1px;
  }

  /* Back */
  .card--back { top: 630px; }
  .back-band {
    position: absolute;
    left: 0; top: 0;
    width: 100%;
    height: 255px;
    background: var(--brand-red);
    color: var(--paper);
    display: flex;
    flex-direction: column;
    align-items: center;
    justify-content: center;
  }
  .back-name {
    font-size: 76px;
    font-weight: 400;
    letter-spacing: 2px;
    line-height: 1;
  }
  .back-title {
    margin-top: 10px;
    font-size: 40px;
    letter-spacing: 8px;
  }
  .contact-row {
    position: absolute;
    left: 0; bottom: 0;
    width: 100%;
    height: 255px;
    display: flex;
    justify-content: space-around;
    align-items: center;
    padding: 0 30px;
  }
  .contact {
    display: flex;
    flex-direction: column;
    align-items: center;
    gap: 26px;
    color: var(--brand-red);
    font-size: 26px;
  }
  .contact-icon { width: 30px; height: 30px; fill: var(--brand-blue); }
</style>
</head>
<body>
<main class="sheet">

  <section class="card card--front" aria-label="Card front">
    <div class="front-frame">
      <span class="front-mark" aria-hidden="true"></span>
      <span class="front-name">Tavor Kesh</span>
    </div>
  </section>

  <section class="card card--back" aria-label="Card back">
    <div class="back-band">
      <h1 class="back-name">TAVOR KESH</h1>
      <p class="back-title">Pediatric Dentist</p>
    </div>
    <div class="contact-row">
      <div class="contact contact--email">
        <svg class="contact-icon" viewBox="0 0 24 24" aria-hidden="true">
          <path d="M2 5h20v14H2z"/>
          <path d="M2 5l10 8 10-8" fill="none" stroke="#fff" stroke-width="1.6"/>
        </svg>
        <span>hello@tavorkesh-kids.com</span>
      </div>
      <div class="contact contact--phone">
        <svg class="contact-icon" viewBox="0 0 24 24" aria-hidden="true">
          <path d="M6.6 10.8a15 15 0 0 0 6.6 6.6l2.2-2.2c.3-.3.7-.4 1-.2 1.1.4 2.3.6 3.6.6.6 0 1 .4 1 1V20c0 .6-.4 1-1 1A17 17 0 0 1 3 4c0-.6.4-1 1-1h3.5c.6 0 1 .4 1 1 0 1.3.2 2.5.6 3.6.1.3 0 .7-.2 1z"/>
        </svg>
        <span>555-0142-7788</span>
      </div>
      <div class="contact contact--web">
        <svg class="contact-icon" viewBox="0 0 24 24" aria-hidden="true">
          <circle cx="12" cy="12" r="10"/>
          <path d="M2 12h20M12 2c3 3 3 17 0 20M12 2c-3 3-3 17 0 20M4 7h16M4 17h16" fill="none" stroke="#fff" stroke-width="1.3"/>
        </svg>
        <span>www.tavorkesh-kids.com</span>
      </div>
    </div>
  </section>

</main>
</body>
</html>
```